MB's Snack Carnival Banner Ad

I am an outdoor Festival Food Vendor. I need designed a 3.5 x 9.5 Banner that extends over the top of my tent. It needs pole pockets at the top and grommets at bottom.

The food items that I want listed on the banner are: Chicken Tenders w/fries, Grilled Chicken on a stick, Catfish w/Red Beans & Rice, Grilled Tilapia w/Mango Salsa, Bowl of Red Beans & Rice, French Fries, Veggies, Fresh Squeezed Lemonade.

Using some red and yellow with Large readable letters. The Business name is MB's please put somewhere on banner maybe a silhouette or back drop. The name MB's does not have to be the focal point I do not have a physical location, mobile business the foods are what I want to stand out.

Target Market(s)

Festival and concert patrons

Industry/Entity Type

Business

Font styles to use
Sans Serif

Requirements
Must have
• A flowing easy to read menu. Not too busy
Nice to have
• I am an outdoor Festival Food Vendor. I need designed a 3.5 x 9.5 feet Banner that extends over the top of my tent. It needs pole pockets at the top and grommets at bottom. The food items that I want listed on the banner are: Chicken Tenders w/fries, Grilled Chicken on a stick, Catfish w/Red Beans & Rice, Grilled Tilapia w/Mango Salsa, Bowl of Red Beans & Rice, French Fries, Grilled Vegetables, Fresh Squeezed Lemonade. Using some red and yellow with Large readable letters. The Business name is MB's please put somewhere on banner maybe a silhouette or back drop. The name MB's does not have to be the focal point I do not have a physical location, mobile business the foods are what I want to stand out.
Should not have
• No religious background, no pictures of people

```html
<!DOCTYPE html>
<html lang="en">
<head>
<meta charset="utf-8">
<title>MB's Snack Carnival – Festival Tent Banner</title>
<link rel="stylesheet" href="https://fonts.googleapis.com/css2?family=Arimo:wght@700&display=swap">
<style>
  :root {
    --backdrop: #1c1c1c;
    --frame: #ffffff;
    --brand-orange: #f07c22;
    --label-text: #ffffff;
    --fries-yellow: #f2c14a;
    --fries-gold: #e39a2c;
    --fries-light: #f5efe0;
    --tilapia-brown: #b8793a;
    --tilapia-crust: #d9a565;
    --mango-yellow: #f6c21c;
    --salsa-red: #d6323a;
    --herb-green: #4f8a2c;
    --rice-white: #ece6da;
    --bean-red: #8e2a1f;
    --bean-dark: #4a1e14;
    --lemon-yellow: #f1e04a;
    --lemonade-pale: #e6e8b8;
    --lime-green: #6fae2c;
    --table-wood: #7a4a26;
    --tender-crust: #d3913e;
    --tender-dark: #9a5a22;
    --skewer-red: #a23e1e;
    --skewer-dark: #5a2212;
    --catfish-spice: #a9692e;
    --catfish-dark: #6e3e1a;
  }
  * { box-sizing: border-box; margin: 0; padding: 0; }
  html, body {
    width: 1200px; height: 678px; overflow: hidden;
    background: var(--backdrop);
  }
  .banner {
    position: absolute;
    left: 48px; top: 139px;
    width: 1097px; height: 403px;
    background: var(--frame);
    padding: 4px;
    display: grid;
    grid-template-columns: repeat(4, 1fr);
    grid-template-rows: repeat(2, 1fr);
    gap: 4px 7px;
  }
  .menu-item { position: relative; overflow: hidden; }
  .menu-item__photo { position: absolute; inset: 0; }
  .menu-item__band {
    position: absolute; inset: 0;
    background: var(--brand-orange);
    clip-path: polygon(0 86%, 100% 59%, 100% 100%, 0 100%);
  }
  .menu-item__name {
    position: absolute;
    right: 13px; bottom: 9px;
    text-align: right;
    color: var(--label-text);
    font-family: "Arimo", Arial, sans-serif;
    font-weight: 700;
    font-size: 16px;
    line-height: 23px;
    letter-spacing: 0.3px;
  }

  .photo-fries {
    background:
      radial-gradient(ellipse 60% 50% at 30% 45%, var(--fries-yellow), transparent 75%),
      radial-gradient(ellipse 60% 55% at 75% 40%, var(--fries-gold), transparent 75%),
      linear-gradient(170deg, var(--fries-light) 0%, var(--fries-yellow) 55%, var(--fries-gold) 100%);
  }
  .photo-tilapia {
    background:
      radial-gradient(ellipse 22% 30% at 55% 30%, var(--mango-yellow), transparent 80%),
      radial-gradient(ellipse 16% 20% at 45% 55%, var(--salsa-red), transparent 80%),
      radial-gradient(ellipse 14% 18% at 12% 28%, var(--herb-green), transparent 80%),
      radial-gradient(ellipse 70% 40% at 55% 45%, var(--tilapia-crust), transparent 80%),
      linear-gradient(170deg, var(--tilapia-brown), var(--tilapia-crust));
  }
  .photo-beans {
    background:
      radial-gradient(ellipse 45% 35% at 50% 30%, var(--rice-white), transparent 80%),
      radial-gradient(ellipse 45% 35% at 40% 65%, var(--bean-red), transparent 80%),
      linear-gradient(170deg, var(--bean-dark) 0%, var(--rice-white) 45%, var(--bean-red) 100%);
  }
  .photo-lemonade {
    background:
      radial-gradient(ellipse 14% 18% at 72% 30%, var(--lemon-yellow), transparent 80%),
      radial-gradient(ellipse 10% 14% at 88% 45%, var(--lime-green), transparent 80%),
      radial-gradient(ellipse 28% 45% at 35% 45%, var(--lemonade-pale), transparent 80%),
      linear-gradient(170deg, var(--lemonade-pale) 0%, var(--table-wood) 100%);
  }
  .photo-tenders {
    background:
      radial-gradient(ellipse 50% 40% at 35% 45%, var(--tender-crust), transparent 80%),
      radial-gradient(ellipse 18% 35% at 72% 50%, var(--fries-yellow), transparent 80%),
      linear-gradient(170deg, var(--fries-light) 0%, var(--tender-crust) 50%, var(--tender-dark) 100%);
  }
  .photo-skewer {
    background:
      radial-gradient(ellipse 60% 22% at 50% 28%, var(--skewer-red), transparent 80%),
      radial-gradient(ellipse 60% 22% at 50% 58%, var(--skewer-red), transparent 80%),
      linear-gradient(170deg, var(--skewer-dark), var(--skewer-red) 50%, var(--skewer-dark));
  }
  .photo-catfish {
    background:
      radial-gradient(ellipse 45% 40% at 35% 45%, var(--catfish-spice), transparent 80%),
      radial-gradient(ellipse 22% 35% at 78% 35%, var(--rice-white), transparent 80%),
      radial-gradient(ellipse 14% 35% at 93% 45%, var(--bean-red), transparent 80%),
      linear-gradient(170deg, var(--catfish-dark), var(--catfish-spice) 60%, var(--rice-white));
  }

  .brand-panel {
    background: var(--brand-orange);
    display: flex;
    align-items: center;
    justify-content: center;
  }
  .brand-panel__name {
    color: var(--label-text);
    font-family: "Arimo", Arial, sans-serif;
    font-weight: 700;
    font-size: 34px;
    line-height: 1.2;
    text-align: center;
  }
</style>
</head>
<body>
  <main class="banner">
    <article class="menu-item">
      <div class="menu-item__photo photo-fries" role="img" aria-label="Photo of golden french fries"></div>
      <div class="menu-item__band"></div>
      <p class="menu-item__name">French Fries,<br>Veggies</p>
    </article>
    <article class="menu-item">
      <div class="menu-item__photo photo-tilapia" role="img" aria-label="Photo of grilled tilapia fillet topped with mango salsa"></div>
      <div class="menu-item__band"></div>
      <p class="menu-item__name">Grilled Tilapia<br>w/Mango Salsa</p>
    </article>
    <article class="menu-item">
      <div class="menu-item__photo photo-beans" role="img" aria-label="Photo of a bowl of red beans and rice"></div>
      <div class="menu-item__band"></div>
      <p class="menu-item__name">Bowl of Red Beans<br>&amp; Rice</p>
    </article>
    <article class="menu-item">
      <div class="menu-item__photo photo-lemonade" role="img" aria-label="Photo of a glass of fresh lemonade with lemons and limes"></div>
      <div class="menu-item__band"></div>
      <p class="menu-item__name">Fresh Squeezed<br>Lemonade</p>
    </article>
    <article class="menu-item">
      <div class="menu-item__photo photo-tenders" role="img" aria-label="Photo of fried chicken tenders with fries"></div>
      <div class="menu-item__band"></div>
      <p class="menu-item__name">Chicken Tenders<br>w/fries</p>
    </article>
    <article class="menu-item">
      <div class="menu-item__photo photo-skewer" role="img" aria-label="Photo of grilled chicken skewers"></div>
      <div class="menu-item__band"></div>
      <p class="menu-item__name">Grilled Chicken<br>on a stick</p>
    </article>
    <article class="menu-item">
      <div class="menu-item__photo photo-catfish" role="img" aria-label="Photo of blackened catfish with red beans and rice"></div>
      <div class="menu-item__band"></div>
      <p class="menu-item__name">Catfish Grilled/Fried<br>w/Red Beans &amp; Rice</p>
    </article>
    <section class="brand-panel">
      <h1 class="brand-panel__name">MB's<br>Snack Carnival</h1>
    </section>
  </main>
</body>
</html>
```